Personal logo & business cards
for owner of multiple businesses.
Hi qlindo,
I really like your design #16. Can you maybe try it in a couple different colour combinations, and maybe also with the 'MIRELA VOSK' part in a cursive text?
Thanks,
Mirela
Hello porvadesign:
I like the design on 19 & 20, but I'd prefer it without the logo on the front. Also, there's maybe too much purple... it's a bit too feminine. Can you try it with less purple or in another colour?
Thanks!
I don't currently have a logo or anything... and would prefer that there wasn't a logo for one of my businesses on the front of my card. A personal logo would be okay though.
@PH - Any logo to use? Thanks
Hey everyone,
Please make sure to read the brief a little more closely. I only want my name and personal contact information on the front of the card, and the names of the THREE businesses that I am involved in on the back of the card.
Thanks for your submissions!
Open to colour palette, but leaning more towards purple or green. No blues.

```html
<!DOCTYPE html>
<html lang="en">
<head>
<meta charset="utf-8">
<title>Mirela Vosk – Business Cards</title>
<link rel="stylesheet" href="https://fonts.googleapis.com/css2?family=Arimo:wght@400;700&display=swap">
<style>
  :root {
    --backdrop: #4a4526;
    --card-white: #ffffff;
    --card-black: #0b0b0b;
    --pink: #e5197a;
    --pink-deep: #b80f5e;
    --pink-soft: #f27bb1;
    --ink: #2b2b2b;
    --ink-soft: #555555;
    --lime: #9bc63b;
    --charcoal: #3a3a3a;
  }
  * { box-sizing: border-box; margin: 0; padding: 0; }
  html, body { width: 1200px; height: 1009px; overflow: hidden; }
  body {
    background: var(--backdrop);
    font-family: "Arimo", Arial, sans-serif;
    position: relative;
  }
  .card {
    position: absolute;
    border-radius: 26px;
    overflow: hidden;
    box-shadow: 0 6px 18px rgba(0,0,0,0.45);
  }
  /* Front */
  .card--front {
    left: 494px; top: 115px; width: 547px; height: 455px;
    background: var(--card-white);
  }
  .card--front .swoosh { position: absolute; inset: 0; }
  .front-title {
    position: absolute; left: 28px; top: 14px;
    color: var(--card-white); font-weight: 700; font-size: 25px;
  }
  .puzzle-art {
    position: absolute; border-radius: 14px;
  }
  .card--front .puzzle-art {
    left: 356px; top: 20px; width: 130px; height: 150px;
    background: linear-gradient(135deg, var(--charcoal) 0%, var(--pink) 50%, var(--lime) 100%);
    clip-path: polygon(25% 0, 60% 5%, 80% 25%, 100% 55%, 85% 95%, 50% 90%, 10% 100%, 0 55%, 15% 25%);
  }
  .front-name {
    position: absolute; left: 191px; top: 170px;
    color: var(--ink); font-weight: 700; font-size: 33px; letter-spacing: 0.5px;
  }
  .contact {
    position: absolute; left: 191px; top: 212px;
    list-style: none; color: var(--ink-soft); font-size: 17.5px; line-height: 25px;
  }
  .contact li { display: flex; align-items: center; gap: 8px; }
  .contact .addr { display: block; padding-left: 0; }
  .contact svg { width: 16px; height: 16px; flex: none; }
  /* Back */
  .card--back {
    left: 184px; top: 548px; width: 553px; height: 345px;
    background: var(--card-black);
  }
  .ventures {
    position: absolute; left: 63px; top: 66px;
    list-style: none; color: var(--pink); font-size: 19px; line-height: 22px;
  }
  .ventures li { margin-bottom: 32px; }
  .card--back .puzzle-art {
    left: 350px; top: 150px; width: 190px; height: 180px;
    background: linear-gradient(135deg, #3a3a3a 0%, var(--pink) 45%, var(--lime) 100%);
    clip-path: polygon(30% 0, 65% 5%, 85% 30%, 100% 60%, 80% 100%, 45% 92%, 5% 100%, 0 60%, 15% 30%);
  }
  .back-web {
    position: absolute; left: 200px; top: 317px;
    display: flex; align-items: center; gap: 6px;
    color: var(--pink); font-size: 12px;
  }
  .back-web .dot { width: 11px; height: 11px; border-radius: 50%; background: var(--pink); }
</style>
</head>
<body>
  <section class="card card--front" aria-label="Business card front">
    <svg class="swoosh" viewBox="0 0 547 455" preserveAspectRatio="none" aria-hidden="true">
      <defs>
        <linearGradient id="pinkWash" x1="0" y1="0" x2="1" y2="1">
          <stop offset="0" stop-color="#ef2c86"/>
          <stop offset="1" stop-color="#b80f5e"/>
        </linearGradient>
      </defs>
      <rect x="0" y="0" width="547" height="52" fill="url(#pinkWash)"/>
      <path d="M0 52 H230 C150 120 120 250 160 455 H0 Z" fill="url(#pinkWash)"/>
      <path d="M230 52 C160 130 135 250 175 455 H160 C120 250 150 120 230 52 Z" fill="#f27bb1" opacity="0.7"/>
    </svg>
    <div class="front-title">Mirela Vosk Trosdan</div>
    <div class="puzzle-art" role="img" aria-label="Cluster of interlocking puzzle pieces in charcoal, pink and lime"></div>
    <h1 class="front-name">MIRELA VOSK</h1>
    <ul class="contact">
      <li class="addr">208, 4419 3 Avenue NE&nbsp; Halden,<br>AB T3K 1P4</li>
      <li><svg viewBox="0 0 16 16"><rect x="4" y="1" width="8" height="14" rx="2" fill="var(--pink)"/></svg>403-555-0182</li>
      <li><svg viewBox="0 0 16 16"><rect x="1" y="5" width="14" height="10" rx="2" fill="var(--pink)"/><rect x="4" y="1" width="8" height="5" fill="var(--pink)"/></svg>403-555-0183</li>
      <li><svg viewBox="0 0 16 16"><rect x="1" y="3" width="14" height="10" rx="1" fill="var(--pink)"/><path d="M1 3 L8 9 L15 3" stroke="#fff" stroke-width="1.5" fill="none"/></svg>mirelatrosdan@me.com</li>
      <li><svg viewBox="0 0 16 16"><circle cx="8" cy="8" r="7" fill="var(--pink)"/><path d="M1 8 H15 M8 1 C4 5 4 11 8 15 M8 1 C12 5 12 11 8 15" stroke="#fff" stroke-width="1" fill="none"/></svg>www.mirelavosk.com</li>
    </ul>
  </section>

  <section class="card card--back" aria-label="Business card back">
    <ul class="ventures">
      <li>Mirela Vosk's Liquidation Supercentre<br>President</li>
      <li>Bright Buys @ Bold Prices<br>President</li>
      <li>Trosdan Group<br>Partner</li>
    </ul>
    <div class="puzzle-art" role="img" aria-label="Cluster of interlocking puzzle pieces in charcoal, pink and lime"></div>
    <div class="back-web"><span class="dot"></span>www.mirelavosk.com</div>
  </section>
</body>
</html>
```